Real Estate agent needs flyer/folder to contain bio and overview of services

I'm including files of the layout of the small folder. The folder is 6 1/2 across and 9 1/2 inches long. It will have a front & back cover and then writing on the 2 inside pages.

I am sending a few files to incorporate into the flyer, 1 new logo to use and 2 files which are coloring ideas.

Colors

Designer to choose colors to be used in the design.

```html
<!DOCTYPE html>
<html lang="en">
<head>
<meta charset="utf-8">
<title>Nora Castellane – Folder Layout</title>
<link href="https://fonts.googleapis.com/css2?family=Crimson+Text:wght@400;700&family=PT+Serif:ital,wght@0,400;0,700;1,400;1,700&family=Ubuntu:wght@400;500;700&family=Montserrat:wght@800&family=Teko:wght@600&display=swap" rel="stylesheet">
<style>
  :root{
    --aqua:#5ff5e3;
    --cyan:#05c6f3;
    --silver:#e3e3e3;
    --peach:#fde0b2;
    --ink:#1c1317;
    --navy:#0a1747;
    --royal:#1f4fe0;
    --gold:#c9a55a;
    --sand:#f4d7a1;
    --rule:#9a9a9a;
    --label:"Crimson Text", serif;
    --serif:"PT Serif", serif;
    --sans:"Ubuntu", sans-serif;
  }
  *{box-sizing:border-box;margin:0;padding:0}
  html,body{width:1200px;height:1196px;overflow:hidden;background:#fff}
  .canvas{position:relative;width:1200px;height:1196px;overflow:hidden;background:#fff;font-family:var(--serif);color:var(--ink)}
  .abs{position:absolute}

  .section-title{position:absolute;font-family:var(--label);font-size:25px;color:#111;transform:translateX(-50%);white-space:nowrap;line-height:1}

  /* front cover */
  .cover-front{left:40px;top:52px;width:369px;height:539px;background:var(--navy);overflow:hidden}
  .cover-front .skyline{position:absolute;left:0;top:0}
  .brand-seal{position:absolute;left:105px;top:211px;width:116px;height:116px;border-radius:50%;background:#d7d7d9;padding:6px}
  .brand-seal .disc{width:100%;height:100%;border-radius:50%;background:#fff;display:flex;flex-direction:column;align-items:center;justify-content:center;font-family:var(--sans);font-weight:700;color:var(--navy);font-size:11px;line-height:1.25;text-align:center}
  .referral-rule{position:absolute;left:233px;top:213px;width:1.5px;height:113px;background:var(--gold)}
  .referral-note{position:absolute;left:239px;top:210px;font-family:var(--serif);font-size:10px;line-height:13.1px;color:#fff;white-space:nowrap}
  .agent-name{position:absolute;left:204px;top:411px;font-family:var(--sans);font-size:16px;color:var(--sand)}
  .contact{position:absolute;left:189px;display:flex;align-items:center;gap:5px;font-family:var(--sans);font-size:12px;color:#fff;white-space:nowrap}
  .contact svg{width:10px;height:10px}
  .ghost-mark{position:absolute;left:40px;top:468px;font-family:var(--sans);font-size:15px;color:#fff;opacity:.1}

  /* cover back / closed flyer face */
  .cover-face{position:absolute;width:368px;height:539px;overflow:hidden}
  .cover-face > svg{position:absolute;left:0;top:0}
  .wordmark{position:absolute;display:flex;align-items:center;gap:6px;font-family:var(--sans);font-weight:500;font-size:17px;color:var(--royal);white-space:nowrap}
  .wordmark .dot{width:9px;height:9px;background:var(--royal)}
  .tagline-small{position:absolute;font-family:var(--sans);font-size:15px;color:#fff}
  .you{position:absolute;font-family:"Montserrat",sans-serif;font-weight:800;line-height:1;letter-spacing:-1px}
  .you .y,.you .u{color:var(--aqua)}
  .you .o{color:var(--peach)}

  .closed-flyer{left:793px;top:632px;border:1px solid #222}

  /* swatches */
  .swatch{position:absolute;width:78px;height:68px;border:1px solid #555}
  .swatch-label{position:absolute;width:120px;text-align:center;font-family:var(--label);font-weight:700;font-size:13.5px;transform:translateX(-50%);white-space:nowrap}

  /* inside spread */
  .spread-lines{position:absolute;left:0;top:0}
  .hi-word{position:absolute;left:84px;top:746px;font-family:"Teko",sans-serif;font-weight:600;font-size:62px;line-height:1;color:#fff;letter-spacing:1px}
  .hi-intro{position:absolute;left:150px;top:754px;font-family:var(--sans);font-size:15px;line-height:20px;color:#fff;white-space:nowrap}
  .tenet-label{position:absolute;left:72px;top:826px;width:72px;height:57px;background:#e4e4e4;font-family:var(--sans);font-size:11.5px;line-height:15px;padding:13px 0 0 9px;color:#222;white-space:nowrap}
  .tenet-you{position:absolute;left:144px;top:826px;width:110px;height:57px;background:var(--navy)}
  .tenet-you .tagline-small{left:9px;top:8px;font-size:9px}
  .tenet-you .you{left:8px;top:18px;font-size:37px}
  .copy{position:absolute;font-family:var(--serif);font-size:7.1px;line-height:9.3px;text-align:justify;color:#222}
  .copy p + p{margin-top:9.3px}
  .copy .stress{color:var(--royal);font-weight:700;font-style:italic}
  .services-title{position:absolute;left:244px;top:952px;transform:translateX(-50%);font-family:var(--sans);font-weight:700;font-size:12.5px;color:var(--navy);white-space:nowrap}
  .services-copy{position:absolute;left:56px;top:977px;width:338px;height:184px;font-family:var(--serif);font-size:6.6px;line-height:7.6px;color:#fff;text-align:justify}
  .services-copy .curve-guard{float:left;width:92px;height:188px;shape-outside:polygon(0 0,7px 0,10px 25px,17px 52px,35px 100px,60px 146px,92px 188px,0 188px)}
  .services-copy p{margin-top:5px}
  .services-copy p:first-of-type{margin-top:0}
  .services-copy h3{font-family:var(--serif);font-weight:700;font-size:11.5px;line-height:13px;color:var(--sand);text-align:left;margin:3px 0 -3px}

  .buying{position:absolute;left:444px;top:667px;font-family:var(--sans);font-weight:700;font-size:12px;color:var(--navy)}
  .home-word{position:absolute;left:447px;top:679px;font-family:"Teko",sans-serif;font-weight:600;font-size:36px;line-height:1;color:var(--navy);letter-spacing:1px}
  .testimonials-title{position:absolute;left:592px;top:902px;transform:translateX(-50%);font-family:var(--serif);font-weight:700;font-size:12.5px;color:var(--navy)}
  .quote-mark{position:absolute;font-family:var(--serif);font-weight:700;font-size:42px;line-height:1;color:#444}
  .testimonial{position:absolute;top:929px;width:102px;background:var(--peach);border:1px solid #e5c68e;padding:3px 4px;font-family:var(--serif);font-size:7.1px;line-height:9.3px;color:#222}
  .testimonial cite{display:block;margin-top:8px;font-style:normal;font-family:var(--sans);font-size:7.3px;color:var(--royal)}
</style>
</head>
<body>
<div class="canvas">

  <div class="section-title" style="left:383px;top:22px">cover &amp; cover back</div>
  <div class="section-title" style="left:431px;top:601px">Inside 2 Pages</div>
  <div class="section-title" style="left:979px;top:596px">closed flyer view</div>
  <div class="section-title" style="left:986px;top:196px">COLORS USED</div>

  <!-- FRONT COVER -->
  <section class="abs cover-front">
    <svg class="skyline" width="369" height="539" role="img" aria-label="Faint city skyline photo">
      <defs>
        <linearGradient id="skyFade" x1="0" y1="0" x2="1" y2="1">
          <stop offset="0" stop-color="#2c5b9c" stop-opacity=".55"/>
          <stop offset="1" stop-color="#0a1747" stop-opacity="0"/>
        </linearGradient>
      </defs>
      <path d="M0,133 H55 L150,225 L150,330 L60,420 H0 Z" fill="url(#skyFade)"/>
    </svg>
    <div class="brand-seal"><div class="disc">Summit Crest<br>Realty</div></div>
    <div class="referral-rule"></div>
    <div class="referral-note">Along with being your<br>Realtor, I'm a lifelong<br>resource for all things<br>home-related &amp;<br>beyond...if you need a<br>great referral for<br>anything at all, call<br>me!&nbsp; I can't wait to<br>work with you!</div>
    <div class="ghost-mark">Nora Castellane</div>
    <div class="agent-name">Nora Castellane</div>
    <div class="contact" style="top:445px">
      <svg viewBox="0 0 10 10"><rect x=".5" y=".5" width="9" height="9" rx="1" fill="#fff"/><path d="M3,2.2 l1.2,1.4 -0.7,.8 c.5,1 1.2,1.7 2.1,2.1 l.8-.7 1.4,1.2 -.9,1 C4.7,7.7 2.4,5.4 2,3.1 Z" fill="#0a1747"/></svg>
      555 014 2287</div>
    <div class="contact" style="top:464px">
      <svg viewBox="0 0 10 10"><rect x=".5" y="1.5" width="9" height="7" fill="#fff"/><path d="M1,2.2 L5,5.5 L9,2.2" stroke="#0a1747" stroke-width=".9" fill="none"/></svg>
      nora@ncastellanehomes.com</div>
    <div class="contact" style="top:483px">
      <svg viewBox="0 0 10 10"><rect x=".5" y=".5" width="9" height="9" fill="#fff"/><circle cx="5" cy="5" r="3.3" stroke="#0a1747" stroke-width=".7" fill="none"/><path d="M1.7,5 H8.3 M5,1.7 V8.3 M5,1.7 C3.4,3.5 3.4,6.5 5,8.3 M5,1.7 C6.6,3.5 6.6,6.5 5,8.3" stroke="#0a1747" stroke-width=".6" fill="none"/></svg>
      www.ncastellanehomes.com</div>
  </section>

  <!-- COVER BACK -->
  <section class="cover-face" style="left:409px;top:52px">
    <svg width="368" height="539">
      <defs>
        <clipPath id="pageA"><path d="M0,0 H282 Q454,269.5 282,539 H0 Z"/></clipPath>
        <linearGradient id="silverA" x1="0" y1="0" x2="1" y2="0"><stop offset="0" stop-color="#fafafa"/><stop offset="1" stop-color="#b9b9b9"/></linearGradient>
        <linearGradient id="cyanA" x1="0" y1="0" x2="1" y2="1"><stop offset="0" stop-color="#1a7cf0"/><stop offset="1" stop-color="#05e6f6"/></linearGradient>
        <linearGradient id="nightA" x1="0" y1="0" x2="0" y2="1"><stop offset="0" stop-color="#0c1f6b"/><stop offset=".55" stop-color="#1b4fc8"/><stop offset="1" stop-color="#0a1747"/></linearGradient>
        <linearGradient id="towerA" x1="0" y1="0" x2="0" y2="1"><stop offset="0" stop-color="#efefef" stop-opacity="0"/><stop offset="1" stop-color="#e2e2e2"/></linearGradient>
      </defs>
      <g clip-path="url(#pageA)">
        <rect width="368" height="539" fill="#fff"/>
        <path d="M0,0 H282 L0,154 Z" fill="url(#silverA)" role="img" aria-label="Silver skyline band"/>
        <path d="M0,0 L42,79 L0,104 Z" fill="url(#cyanA)"/>
        <rect x="0" y="360" width="368" height="179" fill="url(#towerA)" role="img" aria-label="Faint white tower photo"/>
        <path d="M204,183 H368 V356 H274 Q204,356 204,286 V208 Q204,183 229,183 Z" fill="url(#nightA)" role="img" aria-label="Night photo of a community entrance"/>
      </g>
      <path d="M0,0 H282 Q454,269.5 282,539 H0" fill="none" stroke="var(--rule)" stroke-width=".8"/>
    </svg>
    <div class="wordmark" style="left:40px;top:309px"><span class="dot"></span>Nora Castellane</div>
    <div class="tagline-small" style="left:214px;top:227px">It's all about</div>
    <div class="you" style="left:212px;top:245px;font-size:62px"><span class="y">Y</span><span class="o">O</span><span class="u">U</span></div>
  </section>

  <!-- SWATCHES -->
  <div class="swatch" style="left:829px;top:256px;background:var(--aqua)"></div>
  <div class="swatch" style="left:951px;top:256px;background:var(--cyan)"></div>
  <div class="swatch" style="left:1080px;top:256px;background:var(--silver)"></div>
  <div class="swatch" style="left:829px;top:362px;background:var(--peach)"></div>
  <div class="swatch" style="left:951px;top:362px;background:var(--ink)"></div>
  <div class="swatch" style="left:1080px;top:362px;background:var(--navy)"></div>
  <div class="swatch-label" style="left:868px;top:328px">C62 M0 Y9 K0</div>
  <div class="swatch-label" style="left:990px;top:328px">C98 M20 Y0 K0</div>
  <div class="swatch-label" style="left:1119px;top:328px">C0 M0 Y0 K11</div>
  <div class="swatch-label" style="left:868px;top:434px">C0 M12 Y30 K0</div>
  <div class="swatch-label" style="left:990px;top:434px">C70 M80 Y60 K75</div>
  <div class="swatch-label" style="left:1119px;top:434px">C100 M85 Y30 K60</div>

  <!-- INSIDE SPREAD -->
  <svg class="spread-lines" width="1200" height="1196">
    <defs>
      <linearGradient id="facetFade" x1="0" y1="0" x2="0" y2="1">
        <stop offset="0" stop-color="#7fdcf8"/><stop offset=".35" stop-color="#c8f1fc" stop-opacity=".3"/>
        <stop offset=".6" stop-color="#c8f1fc" stop-opacity=".2"/><stop offset="1" stop-color="#7fdcf8"/>
      </linearGradient>
      <linearGradient id="greyFacet" x1="0" y1="0" x2="1" y2="1"><stop offset="0" stop-color="#e6e6e6"/><stop offset="1" stop-color="#fff"/></linearGradient>
      <linearGradient id="portrait" x1="0" y1="0" x2="0" y2="1"><stop offset="0" stop-color="#e6c88a"/><stop offset=".6" stop-color="#d9b493"/><stop offset="1" stop-color="#1e1a1c"/></linearGradient>
      <linearGradient id="poolNight" x1="0" y1="0" x2="0" y2="1"><stop offset="0" stop-color="#1b2a6b"/><stop offset=".45" stop-color="#9a6a2c"/><stop offset="1" stop-color="#1d56d8"/></linearGradient>
    </defs>
    <path d="M127,634 H691 M127,1172 H691 M409,634 V1172" stroke="var(--rule)" stroke-width=".8" fill="none"/>
    <path d="M127,634 Q-47,903 127,1172" stroke="var(--rule)" stroke-width=".8" fill="none"/>
    <path d="M691,634 Q777,760 777,903 Q777,1046 691,1172" stroke="var(--rule)" stroke-width=".8" fill="none"/>
    <path d="M722,634 H777 V1172 H722 Q770,1046 770,903 Q770,760 722,634 Z" fill="url(#facetFade)" role="img" aria-label="Light blue faceted triangle pattern"/>
    <path d="M777,634 V1172" stroke="var(--rule)" stroke-width=".8"/>
    <path d="M127,634 H270 L250,700 L205,744 H70 Q90,690 127,634 Z" fill="url(#greyFacet)" role="img" aria-label="Pale grey faceted pattern"/>
    <rect x="131" y="650" width="76" height="95" rx="30" ry="30" fill="url(#portrait)" role="img" aria-label="Portrait photo of the agent"/>
    <path d="M68,744 H252 Q272,744 272,764 V800 Q272,809 263,809 H55 Q58,775 68,744 Z" fill="var(--ink)"/>
    <path d="M56,973 H397 V1161 H135 Q70,1080 56,973 Z" fill="var(--ink)"/>
    <rect x="522" y="657" width="167" height="88" fill="url(#poolNight)" role="img" aria-label="Photo of a lit luxury home with a pool at night"/>
  </svg>

  <div class="hi-word">HI!</div>
  <div class="hi-intro">It's me<br>Nora Castellane</div>

  <div class="tenet-label">My<br>Core Tenet</div>
  <div class="tenet-you">
    <div class="tagline-small">It's all about</div>
    <div class="you"><span class="y">Y</span><span class="o">O</span><span class="u">U</span></div>
  </div>

  <div class="copy" style="left:72px;top:887px;width:182px">
    <p>My #1 priority is understanding <b>YOUR</b> <span class="stress">needs</span> and <b>YOUR</b> <span class="stress">objectives</span>. This understanding, along with working diligently on your behalf, means we accomplish your goal whether you're purchasing your 1st home or selling a home you've loved so you can move on to the next chapter of your life.</p>
  </div>

  <div class="copy" style="left:277px;top:700px;width:121px">
    <p>I'm originally from Chicago, but I'm a full-fledged California girl now. I've lived and worked in Orange County since 1996. I always say where we live is the next best thing to living on a tropical island. I've traveled to many and I'm always happy to come back to my Laguna Niguel home.</p>
    <p>My passion for this area is why I'm in Real Estate. I consider myself incredibly fortunate to sell homes and help people purchase homes in an area that I love with all my heart.</p>
    <p>This passion also carries over in representing my clients with the highest degree of professionalism, enthusiasm and care. My business is built on exceptional customer service and I'm grateful my clients are mostly repeat and referrals.</p>
  </div>

  <div class="services-title">Real Estate Services &amp; Beyond...</div>
  <div class="services-copy">
    <div class="curve-guard"></div>
    <p>Simply put, I help people who are local, relocating and investing, sell and purchase homes in Southern California. For purchases outside of California, I can refer to a network of agents across the country.</p>
    <p>I also provide a team who is dedicated to providing outstanding customer service throughout the transaction. My team includes a network of lenders, title, and escrow officers, in house CPA, stagers, photographers, contractors and more.</p>
    <h3>Selling your home...</h3>
    <p>Selling your home is not like any other business transaction. It's also personal. My priority as your Listing Agent is to guide you through what can be a complicated and sometimes emotional process.</p>
    <p>I place great emphasis on marketing your property with professional photographs, along with harnessing the power of the Internet and the virtual world to reach as many buyers as possible. Your property will be marketed to the public as well as to other agents, thus creating maximum exposure of your home.</p>
    <p>When we first meet to discuss selling your home, it's essential for me to gain an understanding of your unique needs such as time lines, expectations and financial considerations, just to name a few. From there, I begin the process of listing and marketing your home. I lead you through negotiations and more paperwork than you ever care to do, guiding you to the successful closing of your home.</p>
  </div>

  <div class="buying">Buying a</div>
  <div class="home-word">HOME</div>

  <div class="copy" style="left:437px;top:752px;width:288px">
    <p>If you're thinking about buying a home, it's imperative you have an accomplished, real estate professional by your side to walk you through what is likely the largest purchase of your life.</p>
    <p>To get started, I like to meet with you so we have an opportunity to get to know each other as purchasing a home is a uniquely, personal endeavor. At that time, we can discuss your goals and if it's a good time for you to purchase a home.</p>
    <p>From there, the first step is to obtain a pre-approval from a lender. I'm able to recommend various lenders who can introduce and explain the various loan products available.</p>
    <p>After you've been pre-approved, that's when the fun starts! I guide you through the home buying adventure every step of the way and look forward to handing you the keys to your new home.</p>
  </div>

  <div class="testimonials-title">Testimonials</div>
  <div class="quote-mark" style="left:432px;top:908px">&ldquo;</div>
  <div class="quote-mark" style="left:724px;top:1028px">&rdquo;</div>

  <div class="testimonial" style="left:434px;height:217px">During the home buying process, Nora becomes your trusted advisor, mentor and friend. <b><i>Her knowledge of the industry, community and market are best in class.</i></b> A true professional! Nora aligned her goals with my own and understood the motivation behind my purchase. Nora is unequivocally the reason why I was able to purchase my home in Laguna Niguel and provide my family with a world-class community. Without her guidance and experience, I would still be in the market attempting to navigate the ever-changing work of real estate.<cite>Mara Delacroix</cite></div>
  <div class="testimonial" style="left:540px;height:147px">Nora is the kind of Real Estate professional everyone wants to represent them. She is knowledgeable, ethical, energetic, and follows up on every detail. <b><i>Her honesty, integrity and expertise combined make her a very special and remarkable professional.</i></b> We were lucky to find her!<cite>Henry &amp; Claire Whitlow</cite></div>
  <div class="testimonial" style="left:646px;height:107px">Nora got us an amazing deal on our new home and sold our old home in a week. Nora is patient, hardworking, professional and most importantly HONEST. <b><i>Nora is definitely one of the best in the business!</i></b><cite>Paloma &amp; Adrian Voss</cite></div>

  <!-- CLOSED FLYER -->
  <section class="cover-face closed-flyer">
    <svg width="368" height="539">
      <defs>
        <clipPath id="pageB"><path d="M0,0 H282 Q454,269.5 282,539 H0 Z"/></clipPath>
        <linearGradient id="silverB" x1="0" y1="0" x2="1" y2="0"><stop offset="0" stop-color="#fafafa"/><stop offset="1" stop-color="#b9b9b9"/></linearGradient>
        <linearGradient id="cyanB" x1="0" y1="0" x2="1" y2="1"><stop offset="0" stop-color="#1a7cf0"/><stop offset="1" stop-color="#05e6f6"/></linearGradient>
        <linearGradient id="nightB" x1="0" y1="0" x2="0" y2="1"><stop offset="0" stop-color="#0c1f6b"/><stop offset=".55" stop-color="#1b4fc8"/><stop offset="1" stop-color="#0a1747"/></linearGradient>
        <linearGradient id="towerB" x1="0" y1="0" x2="0" y2="1"><stop offset="0" stop-color="#efefef" stop-opacity="0"/><stop offset="1" stop-color="#e2e2e2"/></linearGradient>
        <linearGradient id="facetB" x1="0" y1="0" x2="0" y2="1">
          <stop offset="0" stop-color="#7fdcf8"/><stop offset=".35" stop-color="#c8f1fc" stop-opacity=".3"/>
          <stop offset=".6" stop-color="#c8f1fc" stop-opacity=".2"/><stop offset="1" stop-color="#7fdcf8"/>
        </linearGradient>
      </defs>
      <path d="M300,0 H368 V539 H300 Q362,400 362,269.5 Q362,139 300,0 Z" fill="url(#facetB)" role="img" aria-label="Light blue faceted triangle pattern"/>
      <g clip-path="url(#pageB)">
        <rect width="368" height="539" fill="#fff"/>
        <path d="M0,0 H282 L0,154 Z" fill="url(#silverB)" role="img" aria-label="Silver skyline band"/>
        <path d="M0,0 L42,79 L0,104 Z" fill="url(#cyanB)"/>
        <rect x="0" y="360" width="368" height="179" fill="url(#towerB)" role="img" aria-label="Faint white tower photo"/>
        <path d="M204,183 H368 V356 H274 Q204,356 204,286 V208 Q204,183 229,183 Z" fill="url(#nightB)" role="img" aria-label="Night photo of a community entrance"/>
      </g>
      <path d="M282,0 Q454,269.5 282,539" fill="none" stroke="var(--rule)" stroke-width=".8"/>
    </svg>
    <div class="wordmark" style="left:40px;top:309px"><span class="dot"></span>Nora Castellane</div>
    <div class="tagline-small" style="left:214px;top:227px">It's all about</div>
    <div class="you" style="left:212px;top:245px;font-size:62px"><span class="y">Y</span><span class="o">O</span><span class="u">U</span></div>
  </section>

</div>
</body>
</html>
```